Etiketten-Design für Trinkweine
Zielgruppe
Wir sind eine Weinkellerei, die einfache Trinkweine für den LEH herstellt.
Unsere Zielgruppen sind Jugendliche .
Wir suchen ein Etikett für unser neues Produkt ,,Traubensaftschorle`` alkoholfrei
Aufgabenstellung
Siehe Anhang , eigene ideen sind auch erwünscht.
Das Etikett sollte Natur verbunden wirken da es ein Bio Produkt ist.
Farben: weiß, grün wären erwünscht.
Das Etikett sollte 75mm hoch und 120mm Breit sein
Strukturpapier weiß
Anbei auch unserer Standartetikett gerne kann das Logo übernommen werden

```html
<!DOCTYPE html>
<html lang="de">
<head>
<meta charset="utf-8">
<title>Traubensaftschorle – Etiketten</title>
<link rel="stylesheet" href="https://fonts.googleapis.com/css2?family=Oswald:wght@200;400;600&display=swap">
<style>
  :root {
    --canvas: #ffffff;
    --ink: #2e2c2d;
    --leaf-green: #8fdf4b;
    --grape-light: #b6ea84;
    --grape-mid: #92da55;
    --paper: #ffffff;
    --frame: #4a4a4a;
  }
  * { box-sizing: border-box; margin: 0; padding: 0; }
  html, body {
    width: 1200px; height: 943px; overflow: hidden;
    background: var(--canvas);
  }
  .sheet {
    position: relative; width: 1200px; height: 943px;
    display: flex; justify-content: center; align-items: center; gap: 80px;
  }
  .label {
    position: relative; width: 388px; height: 620px; overflow: hidden;
    font-family: "Oswald", "Arial Narrow", sans-serif;
    color: var(--ink);
  }
  .label--white { background: var(--paper); border: 1px solid var(--frame); }
  .label--green { background: var(--leaf-green); }

  .label__brand {
    position: absolute; top: 14px; left: 0; right: 0;
    text-align: center; font-weight: 400; font-size: 28px; line-height: 1.1;
    letter-spacing: 0.5px; text-transform: uppercase;
  }
  .label__brand small {
    display: block; font-size: 15px; letter-spacing: 3px; margin-bottom: 2px;
  }
  .label--white .label__brand small { color: var(--grape-mid); }

  .label__grapes {
    position: absolute; top: 90px; left: 20px; width: 368px; height: 400px;
  }
  .label--white .label__grapes {
    background: radial-gradient(ellipse closest-side at 55% 50%, var(--grape-mid) 0%, var(--grape-light) 55%, rgba(182,234,132,0) 100%);
  }
  .label--green .label__grapes {
    background: radial-gradient(ellipse closest-side at 55% 50%, rgba(255,255,255,0.95) 0%, rgba(255,255,255,0.55) 55%, rgba(255,255,255,0) 100%);
  }

  .label__product {
    position: absolute; left: 20px; top: 372px;
    text-transform: uppercase; font-weight: 400;
  }
  .label__product span { display: block; line-height: 76px; }
  .label__product .line-1 { font-weight: 600; font-size: 72px; letter-spacing: -1px; }
  .label__product .line-2 { font-weight: 400; font-size: 64px; }
  .label__product .line-3 { font-weight: 200; font-size: 64px; }

  .label__volume {
    position: absolute; right: 20px; bottom: 26px;
    font-size: 14px; font-weight: 400; color: var(--grape-mid);
  }
  .label--green .label__volume { color: var(--paper); }
</style>
</head>
<body>
<main class="sheet">
  <section class="label label--white">
    <div class="label__brand"><small>Weingut</small>Martin Brauer</div>
    <div class="label__grapes" role="img" aria-label="Grafische Weintraube aus grünen Kreisen mit Blättern"></div>
    <h1 class="label__product">
      <span class="line-1">Trauben</span>
      <span class="line-2">Saft</span>
      <span class="line-3">Schorle</span>
    </h1>
    <div class="label__volume">0,33 l</div>
  </section>

  <section class="label label--green">
    <div class="label__brand"><small>Weingut</small>Martin Brauer</div>
    <div class="label__grapes" role="img" aria-label="Grafische Weintraube aus weißen Kreisen mit Blättern"></div>
    <h2 class="label__product">
      <span class="line-1">Trauben</span>
      <span class="line-2">Saft</span>
      <span class="line-3">Schorle</span>
    </h2>
    <div class="label__volume">0,33 l</div>
  </section>
</main>
</body>
</html>
```